Web design for a french company scanning and analyzing road infrastructures

Tarvix is a French company specializing in the digitization and advanced analysis of road infrastructures.

The current site consists of a single landing page.

We would now like to expand the site to detail the services we offer.

We would therefore like to have several pages created:
- redesign of the home page
- “traffic intersection” study page: Tarvix offers several studies, so we need to create a template for these studies, using the theme of traffic intersections as an example.
- “horizontal marking” service page: The studies are made up of services (simple post-processing). There will be multiple services. Here too, we need to create a template for these services, with the "horizontal marking " service as an example.

Elements to keep (all of them are available in the links below) :
- The Tarvix logo, which must be kept as is, including colors.
- Existing product and service illustrations and videos.
- Existing texts must be kept as they are, in terms of wording and hierarchy, to guarantee the accuracy of the information provided.
- Links to the current "home" (https://tarvix.example/), "traffic intersection" (https://tarvix.example/etudes/intersection/) and "horizontal marking" (https://tarvix.example/post-traitements/signalisation-horizontale-2-2/ ) pages.

Creative guidelines :
- Elegance: Design should communicate elegance while remaining accessible.
- Modernity and Innovation: Draw inspiration from the latest trends in web design to convey our commitment to innovation.
- Content enhancement: The layout should emphasize textual and visual content in a balanced and harmonious way.

To achieve this, you have the option of changing typography, colors (excluding logo), generic illustrations (i.e. not specific to our products and services), and integrating pictograms as required.

Delivery of files :
- Files must be created in Photoshop or Illustrator.
- They must include mock-ups for smartphone, tablet and PC screen resolutions of 1280px and higher.

```html
<!DOCTYPE html>
<html lang="en">
<head>
<meta charset="utf-8">
<title>Tarvix</title>
<link rel="stylesheet" href="https://fonts.googleapis.com/css2?family=Poppins:wght@400;500;600;700;800&display=swap">
<style>
:root{
  --green:#00e04a;
  --green-dark:#038a2c;
  --green-text:#0a8a2e;
  --ink:#333333;
  --body:#555555;
  --light:#f1f1f1;
  --black:#000000;
  --white:#ffffff;
}
*{box-sizing:border-box;margin:0;padding:0}
html,body{width:1200px;height:4461px;overflow:hidden}
body{font-family:'Poppins',sans-serif;color:var(--body);background:var(--white);position:relative}
.abs{position:absolute}
.btn{position:absolute;display:flex;align-items:center;justify-content:center;background:var(--green);color:#053d14;font-weight:700;font-size:15px;text-transform:uppercase;border-radius:0 16px 0 16px;text-decoration:none;letter-spacing:.2px}
.logo{position:absolute;display:flex;align-items:center;gap:12px;color:#0fa83a;font-weight:800;letter-spacing:3px;text-transform:uppercase}
.logo .mark{background:#0fa83a;border-radius:8px}

/* header */
.site-header{position:absolute;left:0;top:0;width:1200px;height:80px;background:var(--white)}
.site-header .logo{left:75px;top:18px;font-size:36px}
.site-header .logo .mark{width:38px;height:38px}
.nav{position:absolute;right:75px;top:30px;display:flex;gap:34px;font-size:13px;font-weight:600;color:var(--ink)}
.nav .active{color:var(--green-text)}

/* hero */
.hero{position:absolute;left:0;top:80px;width:1200px;height:592px;background:#eaeaea}
.hero-img{position:absolute;inset:0;border-bottom-left-radius:260px 340px;background:radial-gradient(ellipse at 20% 60%,#d8a43a 0%,#b2402e 18%,#5a1f5a 32%,#1b2410 55%,#050805 80%);overflow:hidden}
.hero h1{position:absolute;left:0;width:1200px;top:150px;text-align:center;color:var(--white);font-size:98px;font-weight:800;letter-spacing:2px}
.hero-points{position:absolute;left:0;width:1200px;top:270px;text-align:center;color:var(--white);font-size:24px;font-weight:700;line-height:40px}
.hero-points span{display:inline-flex;align-items:center;gap:10px;margin:0 12px}
.hero .btn{left:523px;top:370px;width:156px;height:45px}

/* about */
.about{position:absolute;left:0;top:672px;width:1200px;height:436px;background:linear-gradient(#f8f8f8,#e9e9e9)}
.about-visual{position:absolute;left:68px;top:90px;width:470px;height:290px;border-radius:14px;background:linear-gradient(135deg,#dcdcdc,#9a9a9a 60%,#2a2a2a)}
.about h2{position:absolute;left:615px;top:68px;font-size:40px;font-weight:700;color:var(--ink)}
.about p{position:absolute;left:615px;width:520px;font-size:13.5px;line-height:23px;color:var(--body)}
.about .btn{left:615px;top:311px;width:160px;height:47px}

/* media */
.media-frame{position:absolute;top:1181px;width:512px;height:355px;border:2px solid var(--green);overflow:hidden}
.compare-before{position:absolute;left:0;top:0;width:50%;height:100%;background:linear-gradient(160deg,#3a3a3a,#111)}
.compare-after{position:absolute;right:0;top:0;width:50%;height:100%;background:linear-gradient(160deg,#ff2cf0,#d100d8 70%,#3a8a24);border-left:2px solid var(--green)}
.compare-handle{position:absolute;left:234px;top:150px;width:46px;height:46px;border-radius:50%;background:#29c95a;display:flex;align-items:center;justify-content:center;color:#fff;font-size:16px;font-weight:700}
.video-bg{position:absolute;inset:0;background:linear-gradient(90deg,#060606 0 25%,#7d8a93 25% 62%,#1d2a46 62% 75%,#c0461d 88%,#101010)}
.play{position:absolute;left:228px;top:150px}

/* examples */
.examples{position:absolute;left:0;top:1605px;width:1200px;height:362px;background:var(--green-dark)}
.section-title{position:absolute;left:0;width:1200px;text-align:center;font-weight:700;font-size:38px;letter-spacing:.5px}
.examples .section-title{top:70px;color:var(--white)}
.brand-card{position:absolute;width:242px;height:124px;background:var(--white);border-radius:6px;display:flex;align-items:center;justify-content:center;gap:8px;font-weight:600;font-size:18px;color:var(--ink);text-align:center;line-height:1.2}
.brand-card .dot{width:14px;height:14px;background:var(--green-text);flex:none}
.arrow{position:absolute}

/* post processing */
.post .section-title{top:2025px;color:var(--ink)}
.post-img{position:absolute;top:2116px;width:512px;height:337px;border:2px solid var(--green)}
.post h3{position:absolute;width:512px;top:2474px;text-align:center;font-size:22px;font-weight:700;color:var(--green-text)}
.post p{position:absolute;width:512px;top:2514px;text-align:center;font-size:13px;line-height:24px;color:var(--body)}
.post .btn{top:2612px;width:160px;height:45px}

/* team */
.team{position:absolute;left:0;top:2735px;width:1200px;height:478px;background:var(--green-dark)}
.team .section-title{top:40px;color:var(--white)}
.team p{position:absolute;left:80px;width:1040px;text-align:center;font-size:12.5px;line-height:24px;color:var(--white)}
.partner{position:absolute;top:237px;width:242px;height:92px;background:var(--white);border-radius:6px;display:flex;align-items:center;justify-content:center;gap:8px;font-size:20px;font-weight:600;color:var(--ink)}
.partner .dot{width:14px;height:14px;border-radius:50%;background:#e0303a}
.team .btn{left:523px;top:368px;width:156px;height:45px}

/* clients */
.clients .section-title{top:3283px;color:var(--ink)}
.client-card{position:absolute;top:3378px;width:330px;height:426px;background:var(--light)}
.client-photo{height:245px;border-top-right-radius:90px}
.client-card h3{margin-top:22px;text-align:center;font-size:22px;font-weight:700;color:var(--green-text)}
.client-card p{margin:10px 30px 0;text-align:center;font-size:13px;line-height:22px;color:var(--body)}

/* footer */
.site-footer{position:absolute;left:0;top:3870px;width:1200px;height:591px;background:var(--black);border-top-left-radius:220px 190px;color:var(--white)}
.site-footer .logo{left:78px;top:75px;font-size:36px}
.site-footer .logo .mark{width:38px;height:38px}
.social{position:absolute;right:75px;top:82px;display:flex;gap:16px;font-size:13px;font-weight:600}
.foot-col{position:absolute;top:170px;font-size:12.5px}
.foot-col h4{font-size:14px;font-weight:700;margin-bottom:14px;letter-spacing:.3px}
.foot-col li{list-style:none;line-height:34px}
.foot-col .line{line-height:29px}
.field{position:absolute;background:var(--white);color:#444;font-size:12px;padding:14px 12px}
.site-footer .btn{left:615px;top:450px;width:160px;height:46px}
.copy{position:absolute;left:0;width:1200px;top:555px;text-align:center;font-size:11.5px;color:#cfcfcf}
</style>
</head>
<body>

<header class="site-header">
  <div class="logo"><span class="mark"></span>Tarvix</div>
  <nav class="nav">
    <span class="active">Home</span><span>Product</span><span>Services</span><span>Our Post-Processing</span><span>Our Clients</span><span>Our Team</span><span>Contact</span>
  </nav>
</header>

<section class="hero">
  <div class="hero-img" role="img" aria-label="Colourful 3D point cloud scan of a road at night"></div>
  <h1>TARVIX</h1>
  <div class="hero-points">
    <span><svg width="24" height="24" viewBox="0 0 24 24"><circle cx="12" cy="12" r="10" fill="none" stroke="#fff" stroke-width="2"/><path d="M7 12l3.5 3.5L17 9" fill="none" stroke="#fff" stroke-width="2"/></svg>Unique Technology</span><span><svg width="24" height="24" viewBox="0 0 24 24"><circle cx="12" cy="12" r="10" fill="none" stroke="#fff" stroke-width="2"/><path d="M7 12l3.5 3.5L17 9" fill="none" stroke="#fff" stroke-width="2"/></svg>Topographic Accuracy</span><br>
    <span><svg width="24" height="24" viewBox="0 0 24 24"><circle cx="12" cy="12" r="10" fill="none" stroke="#fff" stroke-width="2"/><path d="M7 12l3.5 3.5L17 9" fill="none" stroke="#fff" stroke-width="2"/></svg>Automated Analysis</span>
  </div>
  <a class="btn" href="https://tarvix.example/">Learn more</a>
</section>

<section class="about">
  <div class="about-visual" role="img" aria-label="Laptop showing the Tarvix software next to the Scanbox scanning unit"></div>
  <h2>TARVIX</h2>
  <p style="top:135px">Resulting from several years of R&amp;D and more than 10 years of expertise in the field of data fusion, the “Scanbox” combines patented positioning system and AI processing automation to digitize the environment with absolute precision, mobile way.</p>
  <p style="top:233px">Our Scanbox integrates advanced 3D scanning technologies and a patented geopositioning system.</p>
  <a class="btn" href="https://tarvix.example/">Learn more</a>
</section>

<div class="media-frame" style="left:75px" role="img" aria-label="Before and after comparison of road markings: grayscale scan and classified point cloud">
  <div class="compare-before"></div><div class="compare-after"></div>
  <div class="compare-handle">‹ ›</div>
</div>
<div class="media-frame" style="left:615px" role="img" aria-label="Video: dashcam road view beside its colour point cloud">
  <div class="video-bg"></div>
  <svg class="play" width="56" height="56" viewBox="0 0 56 56"><circle cx="28" cy="28" r="25" fill="rgba(0,0,0,.35)" stroke="#fff" stroke-width="3"/><path d="M22 17l17 11-17 11z" fill="#fff"/></svg>
</div>

<section class="examples">
  <h2 class="section-title">FOR EXAMPLE</h2>
  <svg class="arrow" style="left:38px;top:148px" width="24" height="40" viewBox="0 0 24 40"><path d="M20 4L4 20l16 16" fill="none" stroke="#fff" stroke-width="3"/></svg>
  <div class="brand-card" style="left:75px;top:156px"><span class="dot"></span>Veltra</div>
  <div class="brand-card" style="left:345px;top:156px"><span class="dot"></span>Ville de<br>Saint-Aubry</div>
  <div class="brand-card" style="left:615px;top:156px"><span class="dot"></span>Technova Lab</div>
  <div class="brand-card" style="left:885px;top:156px"><span class="dot"></span>Val-Armel<br>Département</div>
  <svg class="arrow" style="left:1138px;top:148px" width="24" height="40" viewBox="0 0 24 40"><path d="M4 4l16 16L4 36" fill="none" stroke="#fff" stroke-width="3"/></svg>
</section>

<section class="post">
  <h2 class="section-title">POST-PROCESSING</h2>
  <svg class="arrow" style="left:38px;top:2365px" width="24" height="40" viewBox="0 0 24 40"><path d="M20 4L4 20l16 16" fill="none" stroke="#333" stroke-width="3"/></svg>
  <div class="post-img" style="left:75px;background:linear-gradient(135deg,#6e6e6e,#2b2b2b 55%,#8a8a8a)" role="img" aria-label="Aerial scan of a crossroads with a zoom on worn pedestrian crossings"></div>
  <div class="post-img" style="left:615px;background:linear-gradient(135deg,#1b3fe0,#1a6ff0 45%,#19b6d8 80%,#0a2a9a)" role="img" aria-label="Blue point cloud of a road with detected vertical signs"></div>
  <svg class="arrow" style="left:1138px;top:2365px" width="24" height="40" viewBox="0 0 24 40"><path d="M4 4l16 16L4 36" fill="none" stroke="#333" stroke-width="3"/></svg>
  <h3 style="left:75px">Horizontal Signage</h3>
  <h3 style="left:615px">Vertical Signage</h3>
  <p style="left:75px">Thanks to the digital twin created by our Scanbox, our artificial intelligence algorithms are able to detect and evaluate the state of all horizontal signaling elements present on the scanned lanes.</p>
  <p style="left:615px">Our artificial intelligence algorithms use the digital twin generated by our Scanbox to detect and evaluate the state of vertical signaling elements present on the scanned lanes.</p>
  <a class="btn" style="left:253px" href="https://tarvix.example/post-traitements/signalisation-horizontale-2-2/">Learn more</a>
  <a class="btn" style="left:793px" href="https://tarvix.example/etudes/intersection/">Learn more</a>
</section>

<section class="team">
  <h2 class="section-title">A TEAM OF EXPERTS</h2>
  <p style="top:108px">TARVIX is an operational team made up of around ten engineers from major French schools (École Supérieure d'Ingénierie, ENSA Nord, Polytech Valmont, École des Forges de Paris, Ensor Bretagne, INSTA Rhône), who have more than 10 years of experience experience in cutting-edge technologies and in topography firms.</p>
  <p style="top:165px">Members of the TARVIX R&amp;D team received the prize for the best scientific article on data fusion, the European prize for the best researcher in robotics as well as the Academy of Sciences prize.</p>
  <div class="partner" style="left:75px"><span class="dot"></span>Kelvo</div>
  <div class="partner" style="left:345px"><span class="dot"></span>Finvest</div>
  <div class="partner" style="left:615px"><span class="dot"></span>Nova Seed</div>
  <div class="partner" style="left:885px"><span class="dot"></span>Réseau Bâtir</div>
  <a class="btn" href="https://tarvix.example/">Learn more</a>
</section>

<section class="clients">
  <h2 class="section-title">OUR CLIENTS</h2>
  <article class="client-card" style="left:75px">
    <div class="client-photo" role="img" aria-label="Town hall building with trees under a blue sky" style="background:linear-gradient(#8fb9e6,#c9b48a 55%,#5b7d3a)"></div>
    <h3>Communities</h3>
    <p>We support communities, from the municipality to the department, in their road management and maintenance activities.</p>
  </article>
  <article class="client-card" style="left:436px">
    <div class="client-photo" role="img" aria-label="Surveyor with a total station beside a road" style="background:linear-gradient(#a9c7e3,#7a8a6a 50%,#5a5a5a)"></div>
    <h3>Surveyors</h3>
    <p>We offer surveyors an alternative, efficient and economical solution to traditional scanning methods.</p>
  </article>
  <article class="client-card" style="left:797px">
    <div class="client-photo" role="img" aria-label="Engineer in a safety vest reviewing plans" style="background:linear-gradient(135deg,#3a4a5a,#b8c4cc 55%,#e6e6d8)"></div>
    <h3>Engineering Offices</h3>
    <p>With its ability to scan spaces, TARVIX offers an inventory and management solution for various spaces and their equipment.</p>
  </article>
</section>

<footer class="site-footer">
  <div class="logo"><span class="mark"></span>Tarvix</div>
  <div class="social"><span>Nexo</span><span>Kilo</span><span>Pava</span><span>Lume</span><span>Orbi</span></div>
  <div class="foot-col" style="left:75px">
    <h4>SITE MAP</h4>
    <ul><li>Home</li><li>Product</li><li>Services</li><li>Our post-processing</li><li>Our clients</li><li>Our team</li><li>Contact</li></ul>
  </div>
  <div class="foot-col" style="left:345px">
    <h4>CONTACT INFO</h4>
    <div class="line">12 rue des Ormes</div><div class="line">94210 Valbourg</div><div class="line">contact@tarvix.example</div>
    <h4 style="margin-top:22px">LEGAL</h4>
    <ul><li>Legal Notice</li><li>Privacy Policy</li><li>Cookies policy (EU)</li></ul>
  </div>
  <div class="foot-col" style="left:615px"><h4>CONTACT US</h4></div>
  <div class="field" style="left:615px;top:210px;width:248px;height:46px">First Name</div>
  <div class="field" style="left:879px;top:210px;width:248px;height:46px">Last Name</div>
  <div class="field" style="left:615px;top:270px;width:248px;height:46px">Email Address</div>
  <div class="field" style="left:879px;top:270px;width:248px;height:46px">Phone No</div>
  <div class="field" style="left:615px;top:330px;width:512px;height:106px">Message</div>
  <a class="btn" href="https://tarvix.example/">Submit</a>
  <div class="copy">© 2023 Tarvix. All Right Reserved</div>
</footer>

</body>
</html>
```